Grafic Ad for a Printmagazine about Tractor Vehicles

We need for a Geman Printmagazine about Tractors a Grafic Design in different sizes. Our Website and corporate Design: https://www.kalnoxi.de You can work with the uploaded files . The round Logo with shaking hands should be included in your Designs somehow. Perhaps as a transparent in the background or placed in a corner. The Font used for the URL is Days (glyphvane.com/days.font) Please use this Font or a other similar for the URL "kalnoxi.de" and expand it to "www.kalnoxi.de/traktorwert" For the other Text parts (first line) and (second line) you can use a other font which you prefer. We need the grafics as .jpg in the pixel sizes: 472x496, 437x614, 307x437 (Print would be DPI 300). Goal is a eye-catching design for the later print ad. Have fun and be creative ;)

Logo Text

"Traktor Bewertung" (first line), " Kurzgutachen für Verkauf, Kauf oder Versicherung" (second line), "www.kalnoxi.de/traktorwert" (third line)

Logo styles of interest
Pictorial/Combination Logo
Other font styles liked:
• Days.tff for the URL

Colors
0054AA
0677BA
7BADD7
CADEEF
E8F1F8
0094D4
00A9DD
6FCCEA
C7EBF8
E9F6FB

```html
<!DOCTYPE html>
<html lang="de">
<head>
<meta charset="utf-8">
<title>Traktor Bewertung – Anzeigenformate</title>
<link rel="stylesheet" href="https://fonts.googleapis.com/css2?family=Days+One&family=Source+Sans+3:wght@400&display=swap">
<style>
  :root {
    --sheet-bg: #e6e6e6;
    --brand-blue: #0677BA;
    --brand-deep: #0054AA;
    --sky-1: #E9F6FB;
    --sky-2: #C7EBF8;
    --sky-3: #8fd3f0;
    --title-grey: #555555;
    --brown: #3a2418;
    --url-ink: #3b2a6e;
    --pill-edge: #7BADD7;
  }
  * { margin: 0; padding: 0; box-sizing: border-box; }
  html, body { width: 1200px; height: 2371px; overflow: hidden; }
  body { background: var(--sheet-bg); position: relative; font-family: "Days One", sans-serif; }

  .ad { position: absolute; overflow: hidden; background: var(--sky-1); }
  .ad > * { position: absolute; }
  .ad__bg { left: 0; top: 0; width: 100%; height: 100%; }

  .brand { display: flex; flex-direction: column; align-items: center; }
  .brand__mark { border-radius: 50%; background: var(--brand-blue); }
  .brand__name { color: var(--brand-blue); font-family: "Days One", sans-serif; line-height: 1; }

  .stars { display: block; }
  .title { color: var(--title-grey); line-height: 1; white-space: nowrap; }
  .title__accent { color: var(--brand-blue); }

  .photo-slot {
    border-radius: 40% 30% 35% 40%;
    background: radial-gradient(ellipse at 50% 50%, #6f9ecb 0%, #4c7fb2 45%, rgba(60,90,120,0.0) 75%);
  }

  .lead { color: var(--brown); line-height: 1; white-space: nowrap; }
  .services { list-style: none; }
  .service { display: flex; align-items: center; color: var(--brown); white-space: nowrap; }
  .service svg { flex: none; }

  .url-pill {
    display: flex; align-items: center; justify-content: center;
    border-radius: 60px;
    background: linear-gradient(180deg, #f3fbfe 0%, #cdeefa 55%, #a3dbf3 100%);
    border: 3px solid #ffffff;
    box-shadow: 4px 6px 8px rgba(40, 90, 140, 0.45), inset 0 -3px 0 var(--pill-edge);
  }
  .url-pill span { color: var(--url-ink); letter-spacing: 0.5px; white-space: nowrap; }

  /* Wide format */
  .ad--wide { left: 96px; top: 94px; width: 990px; height: 704px; }
  .ad--wide .brand { left: 60px; top: 30px; width: 160px; }
  .ad--wide .brand__mark { width: 104px; height: 104px; margin-bottom: 12px; }
  .ad--wide .brand__name { font-size: 26px; }
  .ad--wide .stars { left: 504px; top: 16px; width: 360px; height: 108px; }
  .ad--wide .title { left: 446px; top: 136px; font-size: 47px; }
  .ad--wide .photo-slot { left: 144px; top: 254px; width: 384px; height: 294px; }
  .ad--wide .lead { left: 652px; top: 252px; font-size: 22px; }
  .ad--wide .services { left: 650px; top: 310px; }
  .ad--wide .service { height: 92px; font-size: 24px; gap: 20px; }
  .ad--wide .url-pill { left: 54px; top: 566px; width: 882px; height: 90px; }
  .ad--wide .url-pill span { font-size: 50px; }

  /* Tall format */
  .ad--tall { left: 192px; top: 882px; width: 800px; height: 761px; }
  .ad--tall .brand { left: 36px; top: 40px; width: 190px; }
  .ad--tall .brand__mark { width: 112px; height: 112px; margin-bottom: 14px; }
  .ad--tall .brand__name { font-size: 28px; }
  .ad--tall .stars { left: 339px; top: 32px; width: 358px; height: 107px; }
  .ad--tall .title { left: 522px; top: 154px; font-size: 47px; transform: translateX(-50%); }
  .ad--tall .photo-slot { left: 60px; top: 306px; width: 426px; height: 324px; }
  .ad--tall .column { left: 522px; top: 282px; width: 200px; display: flex; flex-direction: column; align-items: center; }
  .ad--tall .column .lead { position: static; font-size: 20px; margin-bottom: 22px; }
  .ad--tall .service { flex-direction: column; font-size: 27px; gap: 4px; height: 101px; }
  .ad--tall .url-pill { left: 50px; top: 648px; width: 696px; height: 72px; }
  .ad--tall .url-pill span { font-size: 40px; }

  /* Small format */
  .ad--small { left: 239px; top: 1734px; width: 706px; height: 496px; }
  .ad--small .brand { left: 40px; top: 18px; width: 124px; }
  .ad--small .brand__mark { width: 76px; height: 76px; margin-bottom: 10px; }
  .ad--small .brand__name { font-size: 20px; }
  .ad--small .stars { left: 375px; top: 18px; width: 230px; height: 69px; }
  .ad--small .title { left: 492px; top: 93px; font-size: 31px; transform: translateX(-50%); }
  .ad--small .photo-slot { left: 85px; top: 174px; width: 276px; height: 216px; }
  .ad--small .lead { left: 431px; top: 166px; font-size: 18px; }
  .ad--small .services { left: 434px; top: 212px; }
  .ad--small .service { height: 70px; font-size: 18px; gap: 14px; }
  .ad--small .url-pill { left: 47px; top: 404px; width: 612px; height: 62px; }
  .ad--small .url-pill span { font-size: 35px; }

  .caption {
    position: absolute; left: 0; width: 1184px; top: 2280px; text-align: center;
    font-family: "Source Sans 3", sans-serif; font-size: 29px; color: #1a1a1a;
  }
</style>
</head>
<body>

<svg width="0" height="0" style="position:absolute" aria-hidden="true">
  <defs>
    <linearGradient id="star-fill" x1="0" y1="0" x2="0" y2="1">
      <stop offset="0" stop-color="#6fb8ea"/>
      <stop offset="1" stop-color="#1f7fcf"/>
    </linearGradient>
    <linearGradient id="sky-fill" x1="0" y1="0" x2="0" y2="1">
      <stop offset="0" stop-color="#E9F6FB"/>
      <stop offset="0.55" stop-color="#C7EBF8"/>
      <stop offset="1" stop-color="#8fd3f0"/>
    </linearGradient>
    <linearGradient id="swoosh-fill" x1="0" y1="0" x2="1" y2="0">
      <stop offset="0" stop-color="#9ed8f2"/>
      <stop offset="1" stop-color="#d8f1fb"/>
    </linearGradient>
    <symbol id="star" viewBox="0 0 100 96">
      <polygon points="50,0 62,35 99,35 69,57 80,94 50,72 20,94 31,57 1,35 38,35" fill="url(#star-fill)"/>
    </symbol>
    <symbol id="icon-tag" viewBox="0 0 40 40">
      <path d="M6 6h14l16 16-14 14L6 20z" fill="none" stroke="currentColor" stroke-width="2.5" stroke-linejoin="round"/>
      <circle cx="13" cy="13" r="3" fill="none" stroke="currentColor" stroke-width="2"/>
      <path d="M18 24l8-8" stroke="currentColor" stroke-width="2"/>
    </symbol>
    <symbol id="icon-money" viewBox="0 0 40 40">
      <rect x="8" y="4" width="18" height="30" rx="2" fill="none" stroke="currentColor" stroke-width="2.5"/>
      <path d="M17 12v12M20 14h-4a2 2 0 0 0 0 4h2a2 2 0 0 1 0 4h-4" fill="none" stroke="currentColor" stroke-width="2"/>
      <path d="M24 26l6 4v8" fill="none" stroke="currentColor" stroke-width="2.5" stroke-linecap="round"/>
    </symbol>
    <symbol id="icon-shield" viewBox="0 0 40 40">
      <path d="M20 3l14 5v10c0 10-6 16-14 19C12 34 6 28 6 18V8z" fill="none" stroke="currentColor" stroke-width="2.5" stroke-linejoin="round"/>
      <path d="M13 20l5 5 9-10" fill="none" stroke="currentColor" stroke-width="2.5" stroke-linecap="round" stroke-linejoin="round"/>
    </symbol>
    <symbol id="star-row" viewBox="0 0 300 90">
      <use href="#star" x="0" y="28" width="60" height="58"/>
      <use href="#star" x="50" y="12" width="76" height="73"/>
      <use href="#star" x="104" y="0" width="92" height="88"/>
      <use href="#star" x="174" y="12" width="76" height="73"/>
      <use href="#star" x="240" y="28" width="60" height="58"/>
    </symbol>
  </defs>
</svg>

<!-- Wide format -->
<section class="ad ad--wide">
  <svg class="ad__bg" viewBox="0 0 990 704" preserveAspectRatio="none" aria-hidden="true">
    <rect width="990" height="704" fill="url(#sky-fill)"/>
    <path d="M0 0H990V196C760 200 520 218 320 244C190 262 80 250 0 236Z" fill="#ffffff"/>
    <path d="M0 164C40 220 170 246 260 250C170 262 60 250 0 232Z" fill="url(#swoosh-fill)"/>
    <path d="M640 208C800 190 920 188 990 190V238C930 214 780 206 640 208Z" fill="#c9ecf9"/>
  </svg>
  <div class="brand"><span class="brand__mark"></span><span class="brand__name">kalnoxi.de</span></div>
  <svg class="stars" viewBox="0 0 300 90" aria-label="Fünf Sterne"><use href="#star-row"/></svg>
  <h1 class="title">Traktor <span class="title__accent">Bewertung</span></h1>
  <div class="photo-slot" role="img" aria-label="Freigestelltes Foto eines hellblauen Oldtimer-Traktors"></div>
  <p class="lead">Kurzgutachen für</p>
  <ul class="services">
    <li class="service"><svg width="40" height="40"><use href="#icon-tag"/></svg>Verkauf</li>
    <li class="service"><svg width="40" height="40"><use href="#icon-money"/></svg>Kauf</li>
    <li class="service"><svg width="40" height="40"><use href="#icon-shield"/></svg>Versicherung</li>
  </ul>
  <div class="url-pill"><span>www.kalnoxi.de/traktorwert</span></div>
</section>

<!-- Tall format -->
<section class="ad ad--tall">
  <svg class="ad__bg" viewBox="0 0 800 761" preserveAspectRatio="none" aria-hidden="true">
    <rect width="800" height="761" fill="url(#sky-fill)"/>
    <path d="M0 0H800V238C620 244 430 250 300 260C180 270 70 262 0 248Z" fill="#ffffff"/>
    <path d="M0 190C40 240 150 256 270 254C170 270 60 262 0 244Z" fill="url(#swoosh-fill)"/>
    <path d="M540 228C660 222 750 222 800 226V282C740 252 640 232 540 228Z" fill="#c9ecf9"/>
  </svg>
  <div class="brand"><span class="brand__mark"></span><span class="brand__name">kalnoxi.de</span></div>
  <svg class="stars" viewBox="0 0 300 90" aria-label="Fünf Sterne"><use href="#star-row"/></svg>
  <h1 class="title">Traktor <span class="title__accent">Bewertung</span></h1>
  <div class="photo-slot" role="img" aria-label="Freigestelltes Foto eines hellblauen Oldtimer-Traktors"></div>
  <div class="column">
    <p class="lead">Kurzgutachen für</p>
    <ul class="services">
      <li class="service"><svg width="46" height="46"><use href="#icon-tag"/></svg>Verkauf</li>
      <li class="service"><svg width="46" height="46"><use href="#icon-money"/></svg>Kauf</li>
      <li class="service"><svg width="46" height="46"><use href="#icon-shield"/></svg>Versicherung</li>
    </ul>
  </div>
  <div class="url-pill"><span>www.kalnoxi.de/traktorwert</span></div>
</section>

<!-- Small format -->
<section class="ad ad--small">
  <svg class="ad__bg" viewBox="0 0 706 496" preserveAspectRatio="none" aria-hidden="true">
    <rect width="706" height="496" fill="url(#sky-fill)"/>
    <path d="M0 0H706V140C540 146 390 156 260 166C160 174 60 168 0 160Z" fill="#ffffff"/>
    <path d="M0 118C40 152 140 166 230 166C150 176 50 170 0 156Z" fill="url(#swoosh-fill)"/>
    <path d="M480 134C590 128 660 128 706 132V172C650 150 570 136 480 134Z" fill="#c9ecf9"/>
  </svg>
  <div class="brand"><span class="brand__mark"></span><span class="brand__name">kalnoxi.de</span></div>
  <svg class="stars" viewBox="0 0 300 90" aria-label="Fünf Sterne"><use href="#star-row"/></svg>
  <h1 class="title">Traktor <span class="title__accent">Bewertung</span></h1>
  <div class="photo-slot" role="img" aria-label="Freigestelltes Foto eines hellblauen Oldtimer-Traktors"></div>
  <p class="lead">Kurzgutachen für</p>
  <ul class="services">
    <li class="service"><svg width="32" height="32"><use href="#icon-tag"/></svg>Verkauf</li>
    <li class="service"><svg width="32" height="32"><use href="#icon-money"/></svg>Kauf</li>
    <li class="service"><svg width="32" height="32"><use href="#icon-shield"/></svg>Versicherung</li>
  </ul>
  <div class="url-pill"><span>www.kalnoxi.de/traktorwert</span></div>
</section>

<p class="caption">CMYK 300 DPI Print File</p>

</body>
</html>
```